Fabric Softener

We need fabric softener. Bottle picture attached for reference. Color of bottle can be proposed as well. Normally bottle is pink and blue color

Logo is also attached that shall be used.

Target Market(s)

Niche

Font styles to use
Sans Serif

Requirements
Must have
• Fabric, Brightness, Nature
Nice to have
• Good colors
Should not have
• Adults

```html
<!DOCTYPE html>
<html lang="en">
<head>
<meta charset="utf-8">
<title>Velora Fabric Softener Label</title>
<link href="https://fonts.googleapis.com/css2?family=Oswald:wght@500;600&display=swap" rel="stylesheet">
<style>
  :root {
    --canvas-bg: #c7aeea;
    --band-purple: #6c5aa9;
    --band-outline: #ffffff;
    --ink-deep: #24105a;
    --glow-white: #ffffff;
  }
  html, body {
    margin: 0;
    padding: 0;
    width: 857px;
    height: 1200px;
    overflow: hidden;
    background: var(--canvas-bg);
  }
  .canvas {
    position: relative;
    width: 857px;
    height: 1200px;
    background: var(--canvas-bg);
  }
  .label {
    position: absolute;
    left: 78px;
    top: 171px;
    width: 700px;
    height: 858px;
  }
  .label-art {
    position: absolute;
    inset: 0;
    width: 700px;
    height: 858px;
  }
  .brand-name {
    position: absolute;
    left: 186px;
    top: 425px;
    width: 470px;
    height: 190px;
    margin: 0;
    text-align: center;
    font-family: "Oswald", sans-serif;
    font-weight: 600;
    font-size: 150px;
    line-height: 190px;
    color: var(--band-outline);
    letter-spacing: 2px;
  }
  .product-type {
    position: absolute;
    left: 261px;
    top: 668px;
    margin: 0;
    font-family: "Oswald", sans-serif;
    font-weight: 600;
    font-size: 36px;
    line-height: 1;
    color: var(--ink-deep);
    white-space: nowrap;
  }
  .freshness-badge {
    position: absolute;
    left: 429px;
    top: 769px;
    width: 76px;
    height: 76px;
    border-radius: 50%;
    border: 2px solid var(--ink-deep);
    background: var(--glow-white);
    box-sizing: border-box;
    display: flex;
    flex-direction: column;
    align-items: center;
    justify-content: center;
    font-family: "Oswald", sans-serif;
    font-weight: 600;
    color: var(--ink-deep);
    line-height: 1;
  }
  .freshness-badge .hours { font-size: 22px; }
  .freshness-badge .caption { font-size: 8px; text-align: center; margin-top: 2px; color: var(--ink-deep); }
  .volume {
    position: absolute;
    left: 520px;
    top: 786px;
    margin: 0;
    font-family: "Oswald", sans-serif;
    font-weight: 600;
    font-size: 40px;
    line-height: 1;
    color: var(--ink-deep);
  }
</style>
</head>
<body>
<main class="canvas">
  <section class="label">
    <svg class="label-art" viewBox="0 0 700 858" xmlns="http://www.w3.org/2000/svg">
      <defs>
        <linearGradient id="roseTones" x1="0" y1="0" x2="1" y2="1">
          <stop offset="0" stop-color="#f4b3a8"/>
          <stop offset="0.35" stop-color="#e07ad8"/>
          <stop offset="0.6" stop-color="#f0a7a6"/>
          <stop offset="1" stop-color="#c95ccc"/>
        </linearGradient>
        <radialGradient id="softGlow" cx="0.5" cy="0.5" r="0.5">
          <stop offset="0" stop-color="#ffffff" stop-opacity="0.95"/>
          <stop offset="0.6" stop-color="#efe6fb" stop-opacity="0.75"/>
          <stop offset="1" stop-color="#d9c6f3" stop-opacity="0"/>
        </radialGradient>
      </defs>
      <g class="floral-photo" role="img" aria-label="Bouquet of pink and magenta roses with green leaves">
        <path d="M0,858 L0,330 C0,150 120,0 230,0 C320,0 360,60 375,130 C395,230 400,300 460,318 L700,340 L700,830 Q700,858 670,858 Z" fill="url(#roseTones)"/>
      </g>
      <ellipse class="label-glow" cx="480" cy="710" rx="280" ry="190" fill="url(#softGlow)"/>
      <path class="brand-band" d="M166,419 C300,395 420,420 520,405 C600,394 660,386 697,384 L692,664 C600,676 480,640 360,645 C270,650 200,670 158,712 Z"
            fill="var(--band-purple)" stroke="var(--band-outline)" stroke-width="6" stroke-linejoin="round"/>
    </svg>
    <h1 class="brand-name">Velora</h1>
    <p class="product-type">FABRIC SOFTNER</p>
    <div class="freshness-badge">
      <span class="hours">24</span>
      <span class="caption">HOUR<br>FRESHNESS</span>
    </div>
    <p class="volume">4L</p>
  </section>
</main>
</body>
</html>
```